KVT Calculator

We have a calculator already created however the design seems to be very boring and bland. The calculators goal is to show graphic designers, web development firms, pr agencies, marketing firms how much revenue they can potentially make by offering a managed social media solution to their clients.

We want a great designer to make the calculator appealing to our audience.

It is an amazing offer and opportunity however I do not believe the current design does it justice

you can view and play with calculator live at http://sandbox.plorvinix.com/qzta/

```html
<!DOCTYPE html>
<html lang="en">
<head>
<meta charset="utf-8">
<title>Managed Social Media Profit Calculator</title>
<link href="https://fonts.googleapis.com/css2?family=PT+Sans:wght@700&family=Arimo:wght@400;700&display=swap" rel="stylesheet">
<style>
:root{
  --page:#333333;
  --page-edge:#1a1a1a;
  --cell:#000000;
  --label:#ffffff;
  --ink:#111111;
  --white:#ffffff;
  --basic:#ffc400;
  --basic-deep:#ff9a00;
  --pro:#6cbc00;
  --pro-deep:#4c9a00;
  --lime:#99ff00;
  --enterprise:#0a55c8;
  --enterprise-deep:#0a3ea0;
  --btn:#d9d9d9;
  --btn-pro:#66b800;
}
*{box-sizing:border-box;margin:0;padding:0}
html,body{width:1200px;height:900px;overflow:hidden}
body{background:var(--page);font-family:"PT Sans",sans-serif;font-weight:700;position:relative;border:1px solid var(--page-edge)}
.abs{position:absolute}
.concrete{left:0;top:788px;width:1200px;height:112px;background:linear-gradient(180deg,#9a9a9a,#7e7e7e 60%,#8a8a8a)}
.panel{left:58px;top:132px;width:1097px;height:536px;border-radius:32px;background:linear-gradient(180deg,#d0d0d0,#8f8f8f 50%,#bdbdbd);padding:6px}
.panel-inner{width:100%;height:100%;border-radius:27px;background:linear-gradient(180deg,#4a4a4a,#3b3b3b)}
.terms-col{left:75px;top:180px;width:177px;height:440px;background:linear-gradient(90deg,#bdbdbd,#e6e6e6 50%,#bdbdbd)}
.terms-head{left:78px;top:150px;width:173px;height:62px;border-radius:16px;background:linear-gradient(180deg,#5a5a5a,#3a3a3a);color:var(--white);font-size:24px;text-align:center;line-height:52px;box-shadow:0 2px 4px rgba(0,0,0,.5);white-space:nowrap}
.label{left:252px;width:276px;height:77px;background:var(--label);color:var(--ink);font-size:22px;padding-left:32px;display:flex;align-items:center;padding-bottom:4px;white-space:nowrap}
.plan{width:194px;height:447px;top:149px;border:3px solid var(--white);border-radius:22px;background:linear-gradient(180deg,#6a6a6a,#3d3d3d 20%,#3d3d3d 80%,#8a8a8a)}
.plan.pro{border-color:var(--lime);background:linear-gradient(180deg,#555,#3d3d3d 20%,#3d3d3d 74%,var(--lime) 74%)}
.pill{position:absolute;left:6px;top:4px;right:6px;height:62px;border-radius:18px;color:var(--white);font-size:24px;text-align:center;line-height:60px;white-space:nowrap}
.basic .pill{background:linear-gradient(160deg,var(--basic-deep),var(--basic) 40%)}
.pro .pill{background:linear-gradient(160deg,var(--pro-deep),var(--pro) 40%)}
.enterprise .pill{background:linear-gradient(160deg,var(--enterprise-deep),var(--enterprise) 40%)}
.cell{position:absolute;left:-1px;right:-1px;height:78px;background:var(--cell);color:var(--white);font-size:24px;display:flex;align-items:center;justify-content:center;border-bottom:1px solid #555;padding-bottom:4px}
.btn{position:absolute;top:24px;width:28px;height:28px;background:var(--btn);border-radius:2px}
.pro .btn{background:var(--btn-pro)}
.btn.minus{left:9px}.btn.plus{right:9px}
.btn::before,.btn.plus::after{content:"";position:absolute;background:var(--ink);left:5px;top:12px;width:18px;height:4px}
.btn.plus::after{left:12px;top:5px;width:4px;height:18px}
.total{left:527px;top:610px;width:609px;height:45px;border-radius:14px;background:var(--cell);color:var(--lime);display:flex;align-items:center;white-space:nowrap}
.total-label{font-family:"Arimo",sans-serif;font-weight:400;font-size:20px;margin-left:19px}
.total-value{font-family:"Arimo",sans-serif;font-weight:700;font-size:30px;margin-left:84px}
</style>
</head>
<body>
<div class="abs concrete" role="img" aria-label="Scratched concrete texture band"></div>

<div class="abs panel"><div class="panel-inner"></div></div>

<div class="abs terms-col"></div>
<svg class="abs" style="left:75px;top:212px" width="177" height="420" viewBox="75 212 177 420">
  <g stroke="#ffffff" stroke-width="2">
    <line x1="90" y1="256" x2="238" y2="256"/><line x1="90" y1="297" x2="238" y2="297"/>
    <line x1="90" y1="339" x2="238" y2="339"/><line x1="90" y1="381" x2="238" y2="381"/>
    <line x1="90" y1="422" x2="238" y2="422"/><line x1="90" y1="464" x2="238" y2="464"/>
    <line x1="90" y1="506" x2="238" y2="506"/><line x1="90" y1="547" x2="238" y2="547"/>
    <line x1="90" y1="589" x2="238" y2="589"/>
  </g>
  <rect x="151" y="229" width="26" height="395" fill="#ffffff" stroke="#000" stroke-width="2"/>
  <defs><radialGradient id="knob" cx="0.45" cy="0.35" r="0.7"><stop offset="0" stop-color="#ffe14a"/><stop offset="1" stop-color="#f29a00"/></radialGradient></defs>
  <circle cx="164" cy="552" r="31" fill="url(#knob)" stroke="#d88600" stroke-width="1"/>
  <path d="M146 558 L164 539 L182 558 Z" fill="#fff8d0"/>
</svg>
<div class="abs terms-head">TERMS (YRS)</div>

<div class="abs label" style="top:245px">Clients per month:</div>
<div class="abs label" style="top:324px">You pay:</div>
<div class="abs label" style="top:403px">Your client pays:</div>
<div class="abs label" style="top:482px">Monthly profit ( year 2):</div>

<div class="abs plan basic" style="left:528px">
  <div class="pill">BASIC</div>
  <div class="cell" style="top:93px"><span class="btn minus"></span>1<span class="btn plus"></span></div>
  <div class="cell" style="top:172px">$197</div>
  <div class="cell" style="top:251px"><span class="btn minus"></span>$297<span class="btn plus"></span></div>
  <div class="cell" style="top:330px">$2400</div>
</div>
<div class="abs plan pro" style="left:736px">
  <div class="pill">PRO</div>
  <div class="cell" style="top:93px"><span class="btn minus"></span>1<span class="btn plus"></span></div>
  <div class="cell" style="top:172px">$279</div>
  <div class="cell" style="top:251px"><span class="btn minus"></span>$497<span class="btn plus"></span></div>
  <div class="cell" style="top:330px">$4800</div>
</div>
<div class="abs plan enterprise" style="left:944px">
  <div class="pill">ENTERPRISE</div>
  <div class="cell" style="top:93px"><span class="btn minus"></span>1<span class="btn plus"></span></div>
  <div class="cell" style="top:172px">$2500</div>
  <div class="cell" style="top:251px"><span class="btn minus"></span>$4000<span class="btn plus"></span></div>
  <div class="cell" style="top:330px">$36000</div>
</div>

<div class="abs total">
  <span class="total-label">Monthly profit by the end of year 2 :</span>
  <span class="total-value">$432200</span>
</div>
</body>
</html>
```